International oil and gas consultancy needs a business card design

We need a business card design for a new oil and gas consultancy business based in Perth Australia. This is a professional services business and needs a moderately conservative type of business card. The business card also needs to be simple and uncluttered. The colour of the business logo is dark red (see attached file).
The front of the card should have a white background and mainly black lettering and perhaps some use of dark red and/or grey (your choice).
The back of the card should have a light grey background with dark red, black and or both dark red & black lettering (your choice).
Please find attached a clear brief of how I would like the business card designed.
Updates

Hello Everyone, I have slightly modified the brief. The main change is to incorporate some dark red and grey colours into the card, while still keeping the black lettering dominant. I have made the changes in the attached detailed brief document. Regards

Please note, the front of the card must say Harbor Ledger Advisory (in addition to the logo).

Industry/Entity Type

Conservative

Requirements
Must have
• brief has been updated. please refer to attachment for details.

Front of the card MUST say Harbor Ledger Advisory (in addition to the logo)

```html
<!DOCTYPE html>
<html lang="en">
<head>
<meta charset="utf-8">
<title>Harbor Ledger Advisory — Business Card</title>
<link rel="stylesheet" href="https://fonts.googleapis.com/css2?family=Exo+2:wght@400;500;700&display=swap">
<style>
  :root {
    --backdrop: #d9dbde;
    --card-white: #ffffff;
    --card-grey: #e4e5e7;
    --brand-red: #921a1d;
    --brand-red-deep: #6e1114;
    --ink: #1d1d1f;
    --ink-soft: #3a3a3d;
  }
  * { margin: 0; padding: 0; box-sizing: border-box; }
  html, body {
    width: 1200px;
    height: 864px;
    overflow: hidden;
    background: var(--backdrop);
    font-family: "Exo 2", sans-serif;
  }
  .card {
    position: absolute;
    left: 100px;
    top: 146px;
    width: 1000px;
    height: 572px;
    overflow: hidden;
    background: linear-gradient(135deg, var(--card-white) 30%, var(--card-grey) 100%);
    box-shadow: 0 10px 30px rgba(0,0,0,0.18);
  }
  .card-shapes {
    position: absolute;
    inset: 0;
    width: 100%;
    height: 100%;
  }
  .brand-name {
    position: absolute;
    left: 300px;
    top: 150px;
    color: var(--brand-red);
    font-weight: 700;
    font-size: 40px;
    line-height: 1.05;
    letter-spacing: 0.5px;
  }
  .contact {
    position: absolute;
    right: 40px;
    top: 118px;
    text-align: right;
    color: var(--ink);
    font-weight: 500;
  }
  .contact-address {
    font-size: 21px;
    line-height: 1.3;
    margin-bottom: 22px;
  }
  .contact-line {
    display: flex;
    justify-content: flex-end;
    align-items: center;
    gap: 10px;
    font-size: 18px;
    line-height: 1;
    margin-bottom: 15px;
  }
  .contact-line svg {
    width: 18px;
    height: 18px;
    fill: var(--ink-soft);
    flex: none;
  }
  .holder {
    position: absolute;
    left: 44px;
    bottom: 52px;
  }
  .holder-name {
    color: var(--card-white);
    font-size: 27px;
    font-weight: 500;
    letter-spacing: 1px;
  }
  .holder-role {
    color: var(--brand-red-deep);
    filter: brightness(0.75);
    font-size: 21px;
    font-weight: 400;
    margin-top: 2px;
  }
</style>
</head>
<body>
  <div class="card">
    <svg class="card-shapes" viewBox="0 0 1000 572" preserveAspectRatio="none" aria-hidden="true">
      <path class="red-field" fill="var(--brand-red)"
            d="M0,110 C60,90 110,80 150,78 C80,160 120,300 420,370 C600,410 820,420 1000,420 L1000,572 L0,572 Z"/>
      <path class="swoosh-line" fill="none" stroke="var(--card-white)" stroke-width="4"
            d="M175,70 C95,150 110,305 440,385 C620,425 800,432 960,432"/>
    </svg>

    <div class="brand-name">Harbor Ledger<br>Advisory</div>

    <div class="contact">
      <p class="contact-address">412.9th floor Quay Tower<br>Harbor Road PER</p>
      <p class="contact-line">08 6100 4270
        <svg viewBox="0 0 24 24"><path d="M6.6 10.8a15 15 0 0 0 6.6 6.6l2.2-2.2c.3-.3.7-.4 1-.2 1.1.4 2.3.6 3.6.6.6 0 1 .4 1 1V20c0 .6-.4 1-1 1A17 17 0 0 1 3 4c0-.6.4-1 1-1h3.5c.6 0 1 .4 1 1 0 1.3.2 2.5.6 3.6.1.3 0 .7-.2 1z"/></svg>
      </p>
      <p class="contact-line">08 6100 4270
        <svg viewBox="0 0 24 24"><path d="M7 1h10a2 2 0 0 1 2 2v18a2 2 0 0 1-2 2H7a2 2 0 0 1-2-2V3a2 2 0 0 1 2-2zm0 3v14h10V4zm5 15.5a1 1 0 1 0 0 2 1 1 0 0 0 0-2z"/></svg>
      </p>
      <p class="contact-line">08 6100 4270
        <svg viewBox="0 0 24 24"><path d="M6 2h9l3 3v5h1a3 3 0 0 1 3 3v7a2 2 0 0 1-2 2H4a2 2 0 0 1-2-2v-7a3 3 0 0 1 3-3h1zm2 2v6h8V6h-2V4zm-1 10v2h2v-2zm4 0v2h2v-2zm4 0v2h2v-2z"/></svg>
      </p>
      <p class="contact-line">info@harborledger.com
        <svg viewBox="0 0 24 24"><path d="M3 5h18a1 1 0 0 1 1 1v12a1 1 0 0 1-1 1H3a1 1 0 0 1-1-1V6a1 1 0 0 1 1-1zm1 2.4V17h16V7.4l-8 5.2z M4.6 7 12 11.8 19.4 7z"/></svg>
      </p>
      <p class="contact-line">www.harborledger.com
        <svg viewBox="0 0 24 24"><path d="M12 2a10 10 0 1 0 0 20 10 10 0 0 0 0-20zm6.9 6h-3a15 15 0 0 0-1.3-3.9A8 8 0 0 1 18.9 8zM12 4c.9 1.2 1.6 2.6 2 4h-4c.4-1.4 1.1-2.8 2-4zM4.3 14a8 8 0 0 1 0-4h3.4a16 16 0 0 0 0 4zm.8 2h3a15 15 0 0 0 1.3 3.9A8 8 0 0 1 5.1 16zm3-8h-3a8 8 0 0 1 4.3-3.9A15 15 0 0 0 8.1 8zM12 20c-.9-1.2-1.6-2.6-2-4h4c-.4 1.4-1.1 2.8-2 4zm2.3-6H9.7a14 14 0 0 1 0-4h4.6a14 14 0 0 1 0 4zm.3 5.9a15 15 0 0 0 1.3-3.9h3a8 8 0 0 1-4.3 3.9zm1.7-5.9a16 16 0 0 0 0-4h3.4a8 8 0 0 1 0 4z"/></svg>
      </p>
    </div>

    <div class="holder">
      <p class="holder-name">DANIEL WHITFORD</p>
      <p class="holder-role">Managing Director</p>
    </div>
  </div>
</body>
</html>
```